Cleaning and Restoration Firm requires a Monthly Newsletter

I would like to begin a monthly newsletter. We have done them in the past, but they have not been professionally designed.

The website is www.brightholtcare.com.au
I have included a file nook link to use pictures, logo, etc
https://www.filetrove.net/sh/pq3m9tr2x81vbn4/QZXrTy7LmKdNe2Wf-Hpo-4sGj?dl=0

I have included some links to old newsletters, just for the ideas
http://email.pulvio.com.au/em/mail/view.php?id=2004417&a=51290&k=ab91f3e
http://email.pulvio.com.au/em/mail/view.php?id=2003862&a=51290&k=7d2e5c1
http://email.pulvio.com.au/em/mail/view.php?id=2003379&a=51290&k=e40b9a6
http://email.pulvio.com.au/em/mail/view.php?id=2002915&a=51290&k=9c8f174

We are introducing the new cleaning work vehicle and restoration work trailer. The work vehicle which has taken 5 months to build followed by another 5 months to completely fit out with the new custom built machine and equipment is a one of a kind unit, never been attempted before.

We can do a special of 10% off all carpet and upholstery cleaning jobs for the next 30 days, must be booked in the next 14 days to qualify. Including commercial jobs.

Reason: Looking for a unique design and idea. Looking for something fresh. HAVE INCREASED THE BUDGET

Target Market(s)

Everyone and anyone, tenants moving out of rentals, retirees and professionals looking after the home, spring cleans, emergency water and fire damage, mould remeedation, pre sale cleans,

Font styles to use
Sans Serif

Requirements
Must have
• I would like a fresh email newsletter that is informative, one that shows more info each month about the cleaning and restoration industry, offering clients plenty useful info without having to read too much.
• Professional template.
• An email and SMS return message that will make it easy for clients to book in a on site consultation or phone quote.
• A mingleboard add, like section
• and quotation or just a phone call for advice as this is needed for all restoration work.
• Also to find out a bit of info about us and link to the current and any future websites.
Nice to have
• Something new and fresh.
• Links, Visit our website, services, contact us, like us on mingleboard
Should not have
• Surprise me!

```html
<!DOCTYPE html>
<html lang="en">
<head>
<meta charset="utf-8">
<title>Brightholt Care Services – October 2015 Newsletter</title>
<link rel="stylesheet" href="https://fonts.googleapis.com/css2?family=Open+Sans:wght@300;400;600;700;800&display=swap">
<style>
:root{
  --blue:#1f5fae;
  --blue-dark:#154a8c;
  --sky:#2f8fd8;
  --pink:#e5177b;
  --ink:#333;
  --grey:#6b6b6b;
  --paper:#ffffff;
  --line:#d9d9d9;
}
*{box-sizing:border-box;margin:0;padding:0}
html,body{width:1200px;height:3164px;overflow:hidden;background:var(--paper)}
body{font-family:"Open Sans",Arial,sans-serif;color:var(--ink);position:relative}
.newsletter{position:absolute;inset:0}

/* header */
.masthead{position:absolute;left:0;top:0;width:1200px;height:168px;background:linear-gradient(180deg,var(--sky),var(--blue));text-align:center;color:#fff}
.masthead h1{font-weight:400;font-size:92px;letter-spacing:4px;line-height:100px;padding-top:10px}
.masthead p{font-size:26px;font-weight:600;margin-top:4px}
.hero{position:absolute;left:0;top:168px;width:1200px;height:192px;background:linear-gradient(90deg,#e9e9ef 0%,#f3d7e7 45%,var(--pink) 100%)}
.brand{position:absolute;left:248px;top:52px;width:230px;height:84px;background:#fff;border-radius:10px;display:flex;align-items:center;gap:12px;padding:0 16px}
.brand .dot{width:40px;height:40px;border-radius:50%;background:var(--blue);flex:none}
.brand span{font-size:20px;font-weight:700;color:var(--blue);line-height:1.15}
.hero-photo{position:absolute;left:600px;top:6px;width:360px;height:180px;border-radius:12px;background:radial-gradient(circle at 50% 60%,#9fd2f3,#5aa9e0 55%,rgba(229,23,123,.2) 100%)}
.subscribe{position:absolute;left:0;top:360px;width:1200px;height:48px;background:var(--pink)}
.subscribe .field{position:absolute;left:248px;top:8px;width:264px;height:32px;background:#fff;font-size:16px;color:#555;padding:5px 12px}
.subscribe .btn{position:absolute;left:520px;top:8px;width:112px;height:32px;background:#f6c8dc;color:var(--pink);font-size:15px;font-weight:700;text-align:center;line-height:32px}

/* about / what's new */
.intro{position:absolute;left:0;top:420px;width:1200px;height:300px}
.intro h2{font-weight:400;font-size:56px;line-height:70px;color:var(--pink);text-align:center;position:absolute;top:0;white-space:nowrap}
.intro .about-h{left:232px;width:276px}
.intro .news-h{left:612px;width:348px}
.about-text{position:absolute;left:240px;top:82px;width:264px;height:212px;overflow:hidden;font-size:14.5px;line-height:1.5;color:var(--grey)}
.about-text p+p{margin-top:14px}
.news-card{position:absolute;left:612px;top:82px;width:348px;height:212px;background:#222}
.news-card .cap{background:var(--blue);color:#fff;font-size:12px;line-height:1.35;padding:4px 8px;height:40px;overflow:hidden}
.news-card .photo{height:172px;background:linear-gradient(135deg,#4a4a4a,#c9a24a 55%,#2a2a2a)}

/* services */
.services{position:absolute;left:0;top:728px;width:1200px;height:1130px}
.services h2{position:absolute;left:612px;width:348px;text-align:center;top:22px;font-weight:300;font-size:58px;color:var(--blue-dark);white-space:nowrap}
.services .lady{position:absolute;left:248px;top:0;width:252px;height:200px;background:radial-gradient(ellipse at 45% 40%,#f2d9c6,#d9e3f0 60%,#fff 90%)}
.service-row{position:absolute;left:0;width:1200px;height:280px}
.service-row .band{position:absolute;left:232px;width:736px;top:64px;height:72px;background:var(--pink)}
.service-row .band::before{content:"";position:absolute;left:0;right:0;top:-12px;height:12px;background:var(--blue)}
.service{position:absolute;top:0;width:250px;text-align:center}
.service .ring{width:200px;height:200px;margin:0 auto;border-radius:50%;border:11px solid var(--blue);box-shadow:0 0 0 5px #fff inset}
.service h3{font-size:12px;font-weight:700;color:var(--blue-dark);line-height:1.3;margin-top:8px;text-transform:uppercase}
.c1{left:215px}.c2{left:475px}.c3{left:735px}

/* special */
.special{position:absolute;left:232px;top:1884px;width:736px;height:216px;background:linear-gradient(180deg,var(--blue),var(--blue-dark))}
.special .tab{position:absolute;left:0;top:0;width:300px;height:52px;background:#2c73c4;color:#fff;font-size:26px;font-weight:700;font-style:italic;padding:8px 24px;white-space:nowrap}
.special .off{position:absolute;left:36px;top:78px;font-size:72px;font-weight:800;color:#fff;line-height:1;white-space:nowrap}
.special .deal{position:absolute;left:370px;top:86px;width:340px;font-size:20px;line-height:1.3;color:#cfe1f5}
.special .note{position:absolute;left:40px;top:176px;font-size:14px;color:#cfe1f5}

/* call */
.call{position:absolute;left:0;top:2124px;width:1200px;text-align:center}
.call h4{font-size:30px;font-weight:700;color:#222;line-height:40px}
.call .phone{font-size:54px;font-weight:700;color:#222;letter-spacing:1px;line-height:70px}

/* social banner */
.social-banner{position:absolute;left:232px;top:2260px;width:736px;height:220px;background:linear-gradient(180deg,#e9eef3,#b4bcc4 70%,#6b6f73)}
.social-banner .fleet{position:absolute;inset:0}
.social-banner .offer{position:absolute;left:0;top:22px;width:736px;text-align:center;font-size:25px;font-weight:700;color:var(--pink);white-space:nowrap}
.social-banner .like{position:absolute;right:30px;bottom:14px;width:130px;height:58px;background:var(--blue);color:#fff;font-size:17px;font-weight:700;text-align:center;padding-top:6px;line-height:1.2}
.social-banner .like small{display:block;font-size:12px;font-weight:400}

/* jobs */
.jobs{position:absolute;left:0;top:2520px;width:1200px;height:320px}
.job{position:absolute;top:0;width:340px}
.job h5{font-size:23px;font-weight:400;margin-bottom:14px;white-space:nowrap}
.job.cleaning{left:240px}.job.cleaning h5{color:var(--blue)}
.job.restore{left:620px}.job.restore h5{color:var(--pink)}
.job.cleaning .photo{width:170px;height:230px;background:linear-gradient(180deg,#3a3a3a,#d8d8d8 60%,#6b6b6b)}
.job.cleaning p{position:absolute;left:186px;top:50px;width:150px;font-size:12px;line-height:1.5;color:var(--grey)}
.job.restore .photo{width:340px;height:150px;background:linear-gradient(135deg,#8d7a5f,#e5dccb 50%,#a0896a)}
.job.restore p{width:340px;font-size:12px;line-height:1.5;color:var(--grey);margin-top:10px}

/* footer */
.more{position:absolute;left:0;top:2872px;width:1200px;text-align:center;font-size:34px;color:#333}
.more a{color:var(--pink);text-decoration:none}
.badges{position:absolute;left:0;top:2950px;width:1200px;display:flex;justify-content:center;gap:26px;align-items:center}
.badge{width:86px;height:86px;border-radius:10px;background:#5e8a3a}
.badge.round{border-radius:50%;background:#d63a3a}
.badges .brand-mini{display:flex;align-items:center;gap:8px;background:#fff;border:2px solid var(--line);border-radius:8px;padding:12px 14px}
.brand-mini .dot{width:26px;height:26px;border-radius:50%;background:var(--blue)}
.brand-mini span{font-size:15px;font-weight:700;color:var(--blue)}
.badge.like{width:130px;height:58px;border-radius:0;background:var(--blue);color:#fff;font-size:16px;font-weight:700;text-align:center;line-height:58px}
.connect{position:absolute;left:0;top:3076px;width:1200px;display:flex;justify-content:center;align-items:center;gap:20px}
.connect h6{font-size:36px;font-weight:400;color:#444;letter-spacing:1px;margin-right:10px}
.connect .net{display:flex;align-items:center;gap:8px;font-size:17px;font-weight:600;color:var(--blue)}
.connect .net i{width:30px;height:30px;border-radius:50%;background:var(--blue);display:block}
.connect .net.red{color:#c9302c}.connect .net.red i{background:#c9302c}
</style>
</head>
<body>
<main class="newsletter">

  <header class="masthead">
    <h1>OCTOBER 2015</h1>
    <p>Professional Cleaners of Carpets, Rugs, Floors and Fine Fabrics.</p>
  </header>

  <section class="hero">
    <div class="brand"><i class="dot"></i><span>Brightholt Care<br>Services</span></div>
    <div class="hero-photo" role="img" aria-label="Bucket of cleaning supplies with gloves and soap bubbles"></div>
  </section>

  <form class="subscribe">
    <div class="field">Enter your email id</div>
    <div class="btn">SUBSCRIBE</div>
  </form>

  <section class="intro">
    <h2 class="about-h">ABOUT US</h2>
    <h2 class="news-h">WHAT'S NEW</h2>
    <div class="about-text">
      <p>Step Dry Carpet Care is one of the original carpet dry cleaning companies established in the region back in the 80's. Back then things were far different but the business was very busy with three vans servicing the suburbs and homes of the city with portable machinery.</p>
      <p>Glen Marlow bought Step Dry Carpet Care in 1995. At that time the focus was on carpet cleaning, upholstery cleaning and</p>
    </div>
    <div class="news-card">
      <div class="cap">Introducing our new work vehicle and restoration trailer, fully fitted out with custom equipment.</div>
      <div class="photo" role="img" aria-label="Technician using moisture detection equipment"></div>
    </div>
  </section>

  <section class="services">
    <div class="lady" role="img" aria-label="Smiling cleaner holding cleaning products"></div>
    <h2>OUR SERVICES</h2>

    <div class="service-row" style="top:212px">
      <div class="band"></div>
      <div class="service c1"><div class="ring" style="background:linear-gradient(135deg,#b98e5a,#e9d7b5)" role="img" aria-label="Building inspection"></div><h3>Building Inspection &amp;<br>Moisture Detection</h3></div>
      <div class="service c2"><div class="ring" style="background:linear-gradient(135deg,#3d6d96,#c9d9e6)" role="img" aria-label="Water damage drying equipment"></div><h3>Water Damage Extraction &amp; Drying<br>Building &amp; Structural Drying<br>Desiccant Dehumidification</h3></div>
      <div class="service c3"><div class="ring" style="background:linear-gradient(135deg,#2b2b2b,#c2693a)" role="img" aria-label="Fire damaged room"></div><h3>Fire &amp; Smoke Restoration<br>Specialised Fire Recovery</h3></div>
    </div>

    <div class="service-row" style="top:522px">
      <div class="band"></div>
      <div class="service c1"><div class="ring" style="background:linear-gradient(135deg,#4d4f55,#b9bcc2)" role="img" aria-label="Pest control technician spraying"></div><h3>Pest Control</h3></div>
      <div class="service c2"><div class="ring" style="background:linear-gradient(135deg,#4a6fa0,#d8dfe8)" role="img" aria-label="Upholstery cleaning on a sofa"></div><h3>Upholstery Cleaning, Repairs<br>&amp; Protection<br>Curtain &amp; Drapery Cleaning</h3></div>
      <div class="service c3"><div class="ring" style="background:linear-gradient(135deg,#6d5a44,#d9c8ad)" role="img" aria-label="Carpet cleaning machine on carpet"></div><h3>Premium Carpet Cleaning,<br>Repairs &amp; Protection<br>Oriental &amp; Area Rug Cleaning</h3></div>
    </div>

    <div class="service-row" style="top:832px">
      <div class="band"></div>
      <div class="service c1"><div class="ring" style="background:linear-gradient(135deg,#8c8c8c,#e6e6e6)" role="img" aria-label="Tile and grout cleaning"></div><h3>Tile &amp; Grout Cleaning and Sealing<br>Natural Stone Cleaning &amp; Sealing<br>Driveway, Path &amp; Patio Cleaning</h3></div>
      <div class="service c2"><div class="ring" style="background:linear-gradient(135deg,#3f7cc4,#e07fae)" role="img" aria-label="Colourful fabric samples"></div><h3>Fabric &amp; Fibre Protection<br>Leather Cleaning &amp; Conditioning<br>Auto and Marine Carpet</h3></div>
      <div class="service c3"><div class="ring" style="background:linear-gradient(135deg,#5a5a3a,#cfcfae)" role="img" aria-label="Mould testing on a wall"></div><h3>Mould Testing &amp; Microbial Lab<br>Analysis &amp; Remediation</h3></div>
    </div>
  </section>

  <section class="special">
    <div class="tab">monthly special*</div>
    <div class="off">10% OFF</div>
    <p class="deal">on carpet and upholstery cleaning jobs for the next 30 days.</p>
    <p class="note">must be booked in the next 14 days to qualify. Including commercial jobs.</p>
  </section>

  <section class="call">
    <h4>CALL FOR ADVICE</h4>
    <p class="phone">4061 5820 / 0412 390 574</p>
  </section>

  <section class="social-banner">
    <div class="fleet" role="img" aria-label="New work vehicle and restoration trailer parked side by side"></div>
    <p class="offer">Avail 10% Discount if you like us on mingleboard</p>
    <div class="like"><small>Like us on</small>mingleboard</div>
  </section>

  <section class="jobs">
    <article class="job cleaning">
      <h5>Cleaning job of the month</h5>
      <div class="photo" role="img" aria-label="Technician in protective suit cleaning a dark room"></div>
      <p>Heavy soiling removed from a rental home with full protective gear and truck mounted extraction.</p>
    </article>
    <article class="job restore">
      <h5>Restoration job of the month</h5>
      <div class="photo" role="img" aria-label="Restored carpeted staircase"></div>
      <p>Step Dry Carpet Care is one of the original carpet dry cleaning companies established in the region back in the 80's. Back then things were far different but the business was very busy with three vans servicing the suburbs and homes with portable machinery.</p>
    </article>
  </section>

  <p class="more">Want to Know more about us <a href="https://www.brightholtcare.com.au">Go to our Website</a></p>

  <div class="badges">
    <div class="badge"></div>
    <div class="badge round"></div>
    <div class="brand-mini"><i class="dot"></i><span>Brightholt Care</span></div>
    <div class="badge like">mingleboard</div>
  </div>

  <footer class="connect">
    <h6>CONNECT TO US</h6>
    <span class="net"><i></i>mingleboard</span>
    <span class="net red"><i></i>clipstream</span>
    <span class="net"><i></i>linkwork</span>
  </footer>

</main>
</body>
</html>
```